Wedding Card Design Project

our wedding is on September 6th. we are looking for an elegant creative design for our wedding cards.

the card has to be BI-folded with and envelope, all of them has to have the design.

Name of the groom: Karim
Name of the bride: Rana
date 6th of September 2013
venue : Blue Cedar hotel

you have to give me  a design for the first page of the card. 

the page inside the card the borders and the writting. 
the envelope were the card will be placed where we will write the name of the guest invited. 

please use your imagination and colors. 

colors preferred: classy plus a little bit of yellow orange and lime green (bit essential )

Target Market(s)

these are friends from all ages from 17 to 60

Industry/Entity Type

Wedding

Requirements
Must have
• bi folder with an envelope.

```html
<!DOCTYPE html>
<html lang="en">
<head>
<meta charset="utf-8">
<title>Karim &amp; Rana — Wedding Invitation</title>
<link href="https://fonts.googleapis.com/css2?family=Cinzel:wght@400;500&family=Great+Vibes&display=swap" rel="stylesheet">
<style>
  :root {
    --paper: #ffffff;
    --damask-light: #f7fbe4;
    --damask-tone: #eef6c8;
    --band-light: #eef7b4;
    --band-deep: #d5e96a;
    --rule-orange: #d9a030;
    --ink-green: #2f9a16;
    --script-green: #3c9c1c;
  }
  * { margin: 0; padding: 0; box-sizing: border-box; }
  html, body { width: 1200px; height: 1200px; overflow: hidden; }
  body { background: var(--paper); }

  .invitation {
    position: relative;
    width: 1200px;
    height: 1200px;
    overflow: hidden;
    font-family: "Cinzel", "Trajan Pro", serif;
    color: var(--ink-green);
  }
  .damask-field {
    position: absolute;
    inset: 0;
    background:
      radial-gradient(ellipse at 30% 25%, var(--damask-tone) 0%, transparent 55%),
      radial-gradient(ellipse at 75% 70%, var(--damask-tone) 0%, transparent 55%),
      var(--damask-light);
  }
  .invitation-lead {
    position: absolute;
    top: 106px;
    left: 160px;
    width: 950px;
    font-size: 27px;
    letter-spacing: 0.2px;
    white-space: nowrap;
  }
  .name-band {
    position: absolute;
    top: 160px;
    left: 0;
    width: 1200px;
    height: 141px;
    background: linear-gradient(90deg, var(--band-light) 0%, var(--band-deep) 45%, var(--band-deep) 100%);
  }
  .name-rule {
    position: absolute;
    top: 307px;
    left: 0;
    width: 1107px;
    height: 8px;
    background: var(--rule-orange);
  }
  .couple-names {
    position: absolute;
    top: 146px;
    left: 330px;
    font-family: "Great Vibes", cursive;
    font-weight: 400;
    font-size: 128px;
    line-height: 1.2;
    color: var(--script-green);
    white-space: nowrap;
  }
  .details {
    position: absolute;
    left: 499px;
    top: 338px;
    font-size: 28px;
    line-height: 45px;
    list-style: none;
  }
  .details p { white-space: nowrap; }
  .details .gap { margin-top: 38px; }
</style>
</head>
<body>
  <main class="invitation">
    <div class="damask-field" role="img" aria-label="Soft pale lime damask pattern covering the card background"></div>

    <p class="invitation-lead">The pleasure of your company is requested at the marriage of</p>

    <div class="name-band" role="img" aria-label="Lime green band with tonal damask pattern"></div>
    <div class="name-rule"></div>
    <h1 class="couple-names">Karim &amp; Rana</h1>

    <section class="details">
      <p>Friday, the sixth of September</p>
      <p>two thousand thirteen</p>
      <p>at four in the afternoon</p>

      <p class="gap">The Blue Cedar Hotel</p>
      <p>24 Orchard Lane</p>
      <p>Millbrook, Vermont 05601</p>

      <p class="gap">reception to follow ceremony</p>

      <p class="gap">Please RSVP by August 25th</p>
      <p>via email: KarimRanaWedding@mailbox.com</p>
    </section>
  </main>
</body>
</html>
```